Design Meadowlark Riding Society's clubhouse Third Gallop Sign

Looking to design the Third Gallop clubhouse signage for Meadowlark Riding Society. This will be a one color metal sign that will be placed on the entrance wall next to the entry door. See attached examples, looking for a vector file.

Would like to incorporate the Meadowlark Riding Society Logo or elements of it but open to other ideas and the name of the clubhouse is the Third Gallop - verbiage can be Meadowlark Riding Society- Club house or open to another term depending on design. This will be used to identify the space that will be used by the players and patrons. the clubhouse will be used by players go to mingle, get drinks and watch polo.

Target Market(s)

polo player club lounge for players and patrons to go mingle have drinks.

Colors

Designer to choose only greyscale colors for use in the design.

Requirements
Must have
• the name - Third Gallop

```html
<!DOCTYPE html>
<html lang="en">
<head>
<meta charset="utf-8">
<title>Third Gallop – Meadowlark Riding Society Clubhouse Sign</title>
<link rel="stylesheet" href="https://fonts.googleapis.com/css2?family=Anton&display=swap">
<style>
  :root {
    --page-bg: #f0f0f0;
    --sign-white: #ffffff;
    --charcoal: #212121;
    --accent-grey: #7a7a7a;
    --shadow: rgba(0, 0, 0, 0.18);
  }
  * { margin: 0; padding: 0; box-sizing: border-box; }
  html, body {
    width: 800px;
    height: 1200px;
    overflow: hidden;
    background: var(--page-bg);
  }
  .sign {
    position: absolute;
    left: 40px;
    top: 168px;
    width: 720px;
    height: 864px;
    background: var(--sign-white);
    box-shadow: 0 10px 30px var(--shadow);
    overflow: hidden;
    font-family: "Anton", "Oswald", sans-serif;
  }
  .sign-header-shape {
    position: absolute;
    left: 0;
    top: 0;
    width: 720px;
    height: 520px;
  }
  .club-name {
    position: absolute;
    left: 0;
    width: 100%;
    top: 170px;
    text-align: center;
    color: var(--sign-white);
    font-weight: 400;
    font-size: 40px;
    line-height: 1.2;
    letter-spacing: 6px;
    text-transform: uppercase;
  }
  .clubhouse-title {
    position: absolute;
    left: 0;
    width: 100%;
    top: 522px;
    text-align: center;
    color: var(--charcoal);
    font-weight: 400;
    font-size: 106px;
    line-height: 1.1;
    text-transform: uppercase;
    letter-spacing: -1px;
    white-space: nowrap;
  }
  .phone-band {
    position: absolute;
    left: 69px;
    top: 640px;
    width: 582px;
    height: 114px;
    background: var(--accent-grey);
    display: flex;
    align-items: center;
    justify-content: center;
  }
  .phone-number {
    color: var(--sign-white);
    font-size: 96px;
    line-height: 1;
    letter-spacing: 1px;
    white-space: nowrap;
  }
  .website {
    position: absolute;
    left: 0;
    width: 100%;
    top: 768px;
    text-align: center;
    color: var(--charcoal);
    font-size: 34px;
    line-height: 1.2;
    letter-spacing: 3px;
    white-space: nowrap;
  }
  .footer-bar {
    position: absolute;
    left: 0;
    bottom: 0;
    width: 100%;
    height: 16px;
    background: var(--charcoal);
  }
</style>
</head>
<body>
  <div class="sign">
    <svg class="sign-header-shape" viewBox="0 0 720 520" aria-hidden="true">
      <path class="header-accent" d="M0,0 H720 V310 C600,562 120,562 0,310 Z" fill="var(--accent-grey)"/>
      <path class="header-panel" d="M0,0 H720 V293 C600,541 120,541 0,293 Z" fill="var(--charcoal)"/>
    </svg>
    <p class="club-name">Meadowlark<br>Riding Society</p>
    <h1 class="clubhouse-title">Third Gallop</h1>
    <div class="phone-band"><span class="phone-number">555-204-7318</span></div>
    <p class="website">www.meadowlarkriding.com</p>
    <div class="footer-bar"></div>
  </div>
</body>
</html>
```